Web Design Project

We are looking for a new site design for the VELTO Canada. The current site can be found at
http://www.veltocanada-example.org/
The URL is provided for reference. We want a completely different look and layout which is shown in the specifications document.
As part of the design, we want a home page, and inside page.
The design you provide will be implemented in Joomla. The design winner will only need to provide the PSD. We anticipate creating the template coding in-house.
However, if you have experience creating Joomla templates, please let us know as we may ask you to bid separately to do that phase of the project.
We've provided a specifications document which includes wireframes of the home page, and inside page. We've also included a logo file.
For the header at the top, as indicated in the specs document, we want to keep the same overall treatment to every page. We want a graphic treatment with the logo for the header area. In this manner, the design will be flexiable and can be used for future years.
For the home page, we've indicated that we'd like to have a slider implemented within the design.
The wireframe is provided to illustrate the placement of content and menu items. The exact dimensions of each component can be revised as you see fit. We are also flexiable if you feel we have missed items.

```html
<!DOCTYPE html>
<html lang="en">
<head>
<meta charset="utf-8">
<title>VELTO Canada</title>
<link href="https://fonts.googleapis.com/css2?family=Roboto+Condensed:wght@400&family=Open+Sans:wght@300;400&family=Righteous&family=Cabin:wght@400;600&display=swap" rel="stylesheet">
<style>
:root{
  --page:#ececec;
  --blue:#5674bf;
  --blue-top:#6584cc;
  --blue-bottom:#4765b0;
  --red:#e0393d;
  --dark:#2e2d2e;
  --text:#333;
  --muted:#8a8a8a;
  --panel:#f7f7f7;
  --line:#d4d4d4;
  --footer:#666;
}
*{box-sizing:border-box;margin:0;padding:0}
html,body{width:957px;height:1200px;overflow:hidden}
body{position:relative;background:var(--page);font-family:Arial,Helvetica,sans-serif;color:var(--text)}
.abs{position:absolute}

/* header */
.brand{left:33px;top:34px;display:flex;align-items:center;gap:10px}
.brand-dot{width:40px;height:40px;border-radius:50%;background:#2f4f9a}
.brand-name{font-family:"Roboto Condensed",sans-serif;font-size:20px;color:#2f4f9a}
.utility{left:558px;top:31px;width:368px;height:40px;display:flex;border:1px solid #c8c8c8;border-radius:2px;background:linear-gradient(#f4f4f4,#dcdcdc)}
.utility a{display:flex;align-items:center;gap:7px;padding:0 12px;font-size:13.5px;color:#333;text-decoration:none;border-right:1px solid #c6c6c6}
.utility a:last-child{border-right:0}
.utility svg{flex:none}

/* main nav */
.mainnav{left:33px;top:98px;width:893px;height:52px;background:linear-gradient(var(--blue-top),var(--blue-bottom));border-bottom:3px solid var(--red);display:flex}
.mainnav a{display:flex;align-items:center;padding:0 17px 0 25px;font-family:"Roboto Condensed",sans-serif;font-size:15.5px;color:#fff;text-decoration:none;border-right:1px solid rgba(255,255,255,.15)}
.mainnav a:last-child{border-right:0}

/* hero slider */
.hero{left:0;top:164px;width:957px;height:353px;background:var(--blue)}
.hero-rule-top{left:33px;top:162px;width:893px;height:2px;background:var(--red)}
.hero-rule-bottom{left:33px;top:516px;width:893px;height:2px;background:var(--red)}
.hero-title{left:109px;top:230px;font-family:"Open Sans",sans-serif;font-weight:300;font-size:33px;color:#fff}
.hero-sub{left:112px;top:262px;font-family:"Righteous",sans-serif;font-size:28px;color:#b6c4e4;letter-spacing:1px}
.hero-copy{left:112px;top:313px;width:340px;font-size:13.5px;line-height:17px;color:#fff}
.hero-photo{left:495px;top:178px;width:309px;height:339px;border-radius:150px 150px 0 0;background:linear-gradient(160deg,#b58a63 0%,#e2bfa3 40%,#3a3740 78%,#25242b 100%)}
.slide-arrow{top:309px;width:40px;height:62px;background:#f3f3f3;display:flex;align-items:center;justify-content:center}
.slide-prev{left:0}.slide-next{left:917px}

/* login */
.login{left:33px;top:542px;width:275px;height:245px;background:#fff;border:1px solid #dadada}
.login label{position:absolute;left:24px;font-size:13.5px;color:#555}
.login .field{position:absolute;left:24px;width:228px;height:31px;background:#f5f5f5;border:1px solid #e6e6e6}
.forgot{position:absolute;left:0;width:100%;top:162px;text-align:center;font-size:10.5px;color:#8a8a8a}
.login-foot{position:absolute;left:0;bottom:0;width:100%;height:51px;background:#f1f4f5;border-top:1px solid #e2e2e2}
.keep{position:absolute;left:25px;top:19px;font-size:10.5px;color:#666;display:flex;align-items:center;gap:5px}
.keep i{width:10px;height:10px;border:1px solid #bbb;background:#fff;display:block}
.login-btn{position:absolute;left:171px;top:10px;width:74px;height:27px;border-radius:14px;background:linear-gradient(#c8e6f8,#98cdee);color:#fff;font-size:12.5px;text-align:center;line-height:27px}

/* side panels */
.panel{left:33px;width:275px;background:var(--panel);border:1px solid #d6d6d6}
.panel-head{height:46px;background:linear-gradient(var(--blue-top),var(--blue-bottom));color:#fff;font-size:13.5px;padding:16px 24px}
.sponsors{top:799px;height:171px}
.sponsors p{padding:14px 15px;font-size:11.8px;line-height:17px;color:#333}
.connected{top:987px;height:116px}
.social{display:flex;align-items:center;gap:10px;padding:19px 16px;font-size:11.5px;color:#333}
.social span{margin-right:5px}
.social i{width:27px;height:27px;border-radius:3px;display:block}
.s1{background:#3b5ea6}.s2{background:#5bc2e6}.s3{background:#1978a9}

/* centre copy with news */
.content{left:318px;top:540px;width:620px;font-size:11.6px;line-height:13.1px;color:#333}
.content p{margin-bottom:13px}
.news{float:right;width:234px;height:211px;margin:2px 0 8px 12px;background:#fff;border:1px solid #d6d6d6;position:relative}
.news-head{height:38px;background:var(--dark);color:#fff;font-size:13px;font-weight:bold;padding:13px 29px;position:relative}
.news-head b,.news-card h3 b{color:var(--red);font-weight:normal}
.news-head::after{content:"";position:absolute;left:166px;bottom:-6px;border:6px solid transparent;border-bottom:0;border-top-color:var(--dark)}
.news-card{position:absolute;left:7px;top:54px;width:219px;height:129px;border:1px solid #dcdcdc;border-radius:2px;padding:8px 12px}
.news-card h3{font-weight:normal;font-size:13px;color:#555;margin-left:8px;margin-bottom:14px}
.news-card p{font-size:10.5px;line-height:13px;margin:0}
.pager{position:absolute;left:20px;top:189px;display:flex;gap:3px}
.pager span{width:21px;height:15px;border:1px solid #ddd;font-size:11px;text-align:center;line-height:13px;color:#aaa;background:#f6f6f6}
.pager .on{background:#e4e4e4;color:#555;border-color:#ccc}

/* regions */
.regions-title{left:321px;top:872px;width:585px;display:flex;align-items:center;gap:16px;font-family:"Cabin",sans-serif;font-size:31px;color:#aaa}
.regions-title::before,.regions-title::after{content:"";flex:1;height:3px;background:linear-gradient(90deg,transparent,#c8c8c8,transparent)}
.region{top:921px;width:144px;height:182px;background:#f6f6f6;border:1px solid #d8d8d8;text-align:center}
.region svg{margin-top:7px}
.region h4{font-family:"Cabin",sans-serif;font-weight:600;font-size:13px;color:#666;margin:3px 0 10px}
.region ul{list-style:none;text-align:left;padding-left:23px;font-size:11.8px;line-height:17.5px;color:#999}

/* footer */
.footer{left:0;top:1122px;width:957px;height:78px;background:var(--footer);border-bottom:3px solid var(--red);text-align:center;color:#fff}
.footer nav{margin-top:13px;font-size:11.8px}
.footer nav a{color:#fff;text-decoration:none}
.footer nav span{margin:0 6px}
.copyright{margin-top:20px;font-size:11px;color:#333}
</style>
</head>
<body>

<header>
  <div class="abs brand"><span class="brand-dot"></span><span class="brand-name">VELTO International</span></div>
  <nav class="abs utility">
    <a href="#"><svg width="17" height="14" viewBox="0 0 17 14"><path d="M8.5 1 1 7.5h2.3V13h4V9h2.4v4h4V7.5H16z" fill="#888"/></svg>Home</a>
    <a href="#"><svg width="18" height="12" viewBox="0 0 18 12"><rect x=".5" y=".5" width="17" height="11" fill="#aaa" stroke="#888"/><path d="M1 1l8 6 8-6" fill="none" stroke="#eee"/></svg>Contact Us</a>
    <a href="#"><svg width="14" height="14" viewBox="0 0 14 14"><circle cx="7" cy="7" r="6.5" fill="#999"/></svg>VELTO International</a>
  </nav>
  <nav class="abs mainnav">
    <a href="#">About</a><a href="#">Board</a><a href="#">Chapters</a><a href="#">Member Space</a><a href="#">Resources &amp; Knowledge</a><a href="#">Sponsorship</a><a href="#">Exihibit</a>
  </nav>
</header>

<section>
  <div class="abs hero"></div>
  <div class="abs hero-rule-top"></div>
  <div class="abs hero-photo" role="img" aria-label="Portrait photo of a smiling woman with long brown hair in a dark jacket"></div>
  <h1 class="abs hero-title">Lorem Ipsum</h1>
  <div class="abs hero-sub">Dolor Soles</div>
  <p class="abs hero-copy">Fugiat dapibus, tellus ac cursus commodo, mauesris con,ntum nibh, ut fermentum mas justo sitters amet risus. Cras mattis cosi sectetut amet fermens etrsaters dimets.</p>
  <div class="abs slide-arrow slide-prev"><svg width="11" height="18" viewBox="0 0 11 18"><path d="M9 2 2 9l7 7" fill="none" stroke="#5674bf" stroke-width="2.2"/></svg></div>
  <div class="abs slide-arrow slide-next"><svg width="11" height="18" viewBox="0 0 11 18"><path d="M2 2l7 7-7 7" fill="none" stroke="#5674bf" stroke-width="2.2"/></svg></div>
  <div class="abs hero-rule-bottom"></div>
</section>

<aside>
  <form class="abs login">
    <label style="top:20px">Username:</label>
    <div class="field" style="top:45px"></div>
    <label style="top:89px">Password:</label>
    <div class="field" style="top:114px"></div>
    <div class="forgot">Forgot your password?</div>
    <div class="login-foot">
      <div class="keep"><i></i>Keep me logged in</div>
      <div class="login-btn">Login</div>
    </div>
  </form>
  <div class="abs panel sponsors">
    <div class="panel-head">Sponsors</div>
    <p>Fugiat dapibus, tellus ac cursus commodo mauesris con,ntum nibh, ut fermentuh mas justo sitters amet risus. Cras mattis cosi sectetut amet fermens etrsaters dimets.</p>
  </div>
  <div class="abs panel connected">
    <div class="panel-head">Stay Connected</div>
    <div class="social"><span>Find Us On:</span><i class="s1"></i><i class="s2"></i><i class="s3"></i></div>
  </div>
</aside>

<main class="abs content">
  <div class="news">
    <div class="news-head">Latest <b>News</b></div>
    <div class="news-card">
      <h3>News <b>One</b></h3>
      <p>Lorem ipsum dolor sit amet, consectetur adipiscing elit. Quisque sed scelerisque diam.Nullam magna risus, porta sed semper quis, porttit</p>
    </div>
    <div class="pager"><span class="on">1</span><span>2</span></div>
  </div>
  <p>Lorem ipsum dolor sit amet, consectetur adipiscing elit. Quisque sed scelerisque diam. Nullam magna risus, porta sed semper quis, porttit or a purus. Phasellus convallis odio eget turpis fermentum sit amet ultricies orci vulputate. Duis vel risus vel nulla euismod condimentum. Aliquam pharetra, sem sit amet vulputate gravida, metus risus hendrerit purus, ac dictum nunc dolor eu quam. Mauris accumsan ligula quis magna auctor rutrum vel congue lectus. Pellentesque et elit massa. Morbi eget lobortis tortor. Ut faucibus congue consequat. Vivamus ne c sollicitudin nisi. Donec pulvinar, urna at posuere pellentesque, leo ero pretium justo, ac accumsan arcu purus ac nibh. Nunc dui quam, facilis vel consectetur et, pretium id eros. Phasellus vulputate elit vel odio cursus varius pulvinar libero posuere. Cras justo nisl, convallis ut ornare et, sodales nec lorem.</p>
  <p>Pellentesque mollis massa a erat condimentum euismod blandit risus tincidunt. Donec vestibulum rutrum magna, ut iaculis turpis dictum a. Morbi imperdiet, augue ut lobortis aliquet, dolor diam hendrerit enim, non viverra sem tellus eu diam. Class aptent taciti sociosqu ad litora torquent per conubia nostra, per inceptos himenaeos. Morbi neque ligula, sagittis ut lobortis nec, dictum ut lacus. Mauris vitae libero nec lacus posuere convallis. Praesent magna odio, rhoncus eget feugiat non, consequat in velit. Duis venenatis luctus quam. Phasellus bibendum quam orci, ut varius magna. Sed tempor consequat blandit. Vestibulum hendrerit imperdiet nisl condimentum pharetra. Duis nisl felis, ullamcorper blandit cursus sit amet, auctor nec nisl. Sed dolor lectus, sagittis et consequat nec, cursus ac m Praesent hendrerit sem arcu, quis luctus sem.</p>
</main>

<section>
  <h2 class="abs regions-title">Regions</h2>
  <div class="abs region" style="left:321px">
    <svg width="56" height="30" viewBox="0 0 56 30"><path d="M2 28 18 6l8 10 8-12 20 24" fill="none" stroke="#bbb" stroke-width="2.5"/></svg>
    <h4>Mountain Pacific</h4><ul><li>First Area</li><li>Second Area</li><li>Third Area</li></ul>
  </div>
  <div class="abs region" style="left:469px">
    <svg width="32" height="30" viewBox="0 0 32 30"><circle cx="16" cy="15" r="14" fill="#bbb"/><path d="M22 15H10m5-6-6 6 6 6" fill="none" stroke="#f6f6f6" stroke-width="3"/></svg>
    <h4>Western</h4><ul><li>First Area</li><li>Second Area</li><li>Third Area</li></ul>
  </div>
  <div class="abs region" style="left:617px">
    <svg width="32" height="30" viewBox="0 0 32 30"><path d="M6 2v27" stroke="#bbb" stroke-width="2.5"/><path d="M7 3h20l-5 6 5 6H7z" fill="#bbb"/></svg>
    <h4>Central</h4><ul><li>First Area</li><li>Second Area</li><li>Third Area</li></ul>
  </div>
  <div class="abs region" style="left:765px">
    <svg width="32" height="30" viewBox="0 0 32 30"><path d="M15 29c1-8 1-14 0-20" stroke="#bbb" stroke-width="3" fill="none"/><path d="M4 8c6-6 16-6 24 0-7-2-11-1-13 1z" fill="#bbb"/></svg>
    <h4>Atlantic</h4><ul><li>First Area</li><li>Second Area</li><li>Third Area</li></ul>
  </div>
</section>

<footer class="abs footer">
  <nav><a href="#">Home</a><span>|</span><a href="#">About Us</a><span>|</span><a href="#">Board</a><span>|</span><a href="#">Member Space</a><span>|</span><a href="#">Space and Knowledge</a><span>|</span><a href="#">Sponsorship</a><span>|</span><a href="#">Resource and Exhibit</a><span>|</span><a href="#">Contact Us</a></nav>
  <div class="copyright">Copyright company inc, All rights reserved.</div>
</footer>

</body>
</html>
```